Business Performance Improvement Book Cover Design Project

We need a book cover design for a new company, based in Eastern Australia, called Varrow Global. We advise clients on process improvement, continuous improvement and business performance improvement, especially in the manufacturing areas and Fast Moving Consumer Goods industries.
We have a written a book designed to demonstrate our very high calibre of knowledge and to use as a marketing tool for prospective clients. We hope to give it out at training seminars and as a comprehensive business card.

Title of the book is: An integrated path to Operational Results Growth.
Subtitle: Shape a Steady Progress method to match your workplace values.
Author: by Martin Varrow
Back Cover: No need for a bar code in this edition. An important aspect is that we will distribute by hand. Text below for back page.

'For the experienced Business Performers, this book is designed to offer an insight into the advantages and an example of an approach to Business Improvement. It is not the only way but it is tried and tested in world class companies and it works. For those new to Continuous Improvement, it offers a helpful introduction to a holistic business improvement system, an overview of important success factors and pitfalls, recommendations on how to implement tools and methods and a quick guide to see when to use which tools. '

'Consultancies are one of many tools management teams can engage and management must make sure the consultants tailor their approach to suit its business needs and culture and not vice versa.'

End of text for back cover.

Business Performance Improvement is also known as or can include:
Continuous Improvement
Process Improvement
Lean Six Sigma
Operational Excellence
Total Productive Maintenance
Harlow Assembly Method
Total Quality Management
Business Process Re engineering
Output Levers
=
Varrow Global

The book size is 175 x 240 mm and will need a 10-15mm bleed. The spine is not known at this stage exactly and will need to be updated once the printing is finished but I suggest a 10mm until I have the exact size.

Our company colours are Pantone 288, R0,G75,B141, C100,M79,Y17,K3. Attached are some other publications that give a sense of what we like to portray, Some words which might add to this are: professional, elegance, quality, sleek.

Reason: After receiving the designs, I realised that I needed to update the brief with more and better quality information for designers to work with.

Target Market(s)

people in the accounting and insolvency industries, production managers and CEOs, Chief Operating Officers, members of the executive team of large companies and GMs of small companies.

Industry/Entity Type

Marketing

Requirements
Must have
• Communicate an image that shows an improvement or increase of something.
Very professional and elegant
Emphasis on the words 'Business Performance Improvement' in the title, subtitle also important
Must appeal to a high-end of the market audience
Nice to have
• Recommendation for your cover to be gloss or matt in print
Image can be indirectly related to money but not specifically
Somehow that it matches or is not so different to the attached brochure
Should not have
• Not be too loud or commercial
Book jacket. WIll be printed as soft cover first run and hard cover 2nd run

```html
<!DOCTYPE html>
<html lang="en">
<head>
<meta charset="utf-8">
<title>An Integrated Path to Operational Results Growth — Book Cover</title>
<link href="https://fonts.googleapis.com/css2?family=Oswald:wght@500;600&family=Libre+Baskerville&display=swap" rel="stylesheet">
<style>
  :root {
    --page-bg: #ffffff;
    --spine-blue: #2e5683;
    --band-blue: #2d5380;
    --title-gold: #ffd21a;
    --text-white: #ffffff;
    --logo-black: #0b0b0d;
    --photo-deep: #0d1522;
    --photo-mid: #1e3a5c;
    --photo-glow: #6fb3e6;
  }
  html, body {
    margin: 0;
    padding: 0;
    width: 1200px;
    height: 1000px;
    overflow: hidden;
    background: var(--page-bg);
  }
  .canvas {
    position: relative;
    width: 1200px;
    height: 1000px;
  }
  .book {
    position: absolute;
    left: 245px;
    top: 50px;
    width: 710px;
    height: 900px;
    display: flex;
  }
  /* Spine */
  .spine {
    position: relative;
    width: 110px;
    height: 900px;
    background: var(--spine-blue);
  }
  .spine__brand {
    height: 70px;
    background: var(--logo-black);
    display: flex;
    align-items: center;
    justify-content: center;
    gap: 5px;
  }
  .spine__brand-mark {
    width: 10px;
    height: 10px;
    background: var(--spine-blue);
  }
  .spine__brand-name {
    font-family: "Oswald", sans-serif;
    font-weight: 500;
    font-size: 12px;
    color: var(--text-white);
    letter-spacing: 0.3px;
  }
  .spine__text {
    position: absolute;
    top: 300px;
    right: 10px;
    writing-mode: vertical-rl;
    display: flex;
    flex-direction: column;
    gap: 6px;
  }
  .spine__title {
    font-family: "Oswald", sans-serif;
    font-weight: 600;
    font-size: 18px;
    line-height: 19px;
    color: var(--title-gold);
    text-transform: uppercase;
    letter-spacing: 0.5px;
    margin: 0;
  }
  .spine__subtitle {
    font-family: "Libre Baskerville", serif;
    font-size: 13px;
    line-height: 16px;
    color: var(--text-white);
    text-transform: uppercase;
    margin: 0;
  }
  /* Front cover */
  .front {
    position: relative;
    width: 600px;
    height: 900px;
  }
  .front__image {
    position: absolute;
    inset: 0 0 70px 0;
    background:
      radial-gradient(ellipse 55% 35% at 70% 22%, rgba(111,179,230,0.55), transparent 70%),
      radial-gradient(ellipse 40% 55% at 75% 65%, rgba(160,120,100,0.35), transparent 70%),
      linear-gradient(180deg, var(--photo-mid) 0%, #142a45 35%, var(--photo-deep) 70%, #0a0f18 100%);
  }
  .front__title {
    position: absolute;
    left: 0;
    right: 0;
    top: 505px;
    margin: 0;
    text-align: center;
    font-family: "Oswald", sans-serif;
    font-weight: 600;
    font-size: 44px;
    line-height: 55px;
    color: var(--title-gold);
    text-transform: uppercase;
    text-shadow: 0 2px 6px rgba(0,0,0,0.6);
  }
  .front__subtitle {
    position: absolute;
    left: 0;
    right: 0;
    top: 738px;
    margin: 0;
    text-align: center;
    font-family: "Libre Baskerville", serif;
    font-size: 19px;
    line-height: 27px;
    color: var(--text-white);
    text-transform: uppercase;
  }
  .front__author-band {
    position: absolute;
    left: 0;
    right: 0;
    bottom: 0;
    height: 70px;
    background: var(--band-blue);
    display: flex;
    align-items: center;
    justify-content: center;
  }
  .front__author {
    font-family: "Oswald", sans-serif;
    font-weight: 600;
    font-size: 29px;
    color: var(--text-white);
    text-transform: uppercase;
    letter-spacing: 0.5px;
  }
</style>
</head>
<body>
<div class="canvas">
  <div class="book">
    <div class="spine">
      <div class="spine__brand">
        <span class="spine__brand-mark"></span>
        <span class="spine__brand-name">Varrow Global</span>
      </div>
      <div class="spine__text">
        <p class="spine__title">An integrated path to operational<br>results growth</p>
        <p class="spine__subtitle">Shape a steady progress method to match your workplace values</p>
      </div>
    </div>
    <div class="front">
      <div class="front__image" role="img" aria-label="Photo of a businessman's finger touching a glowing network of connected people icons on a dark blue background"></div>
      <h1 class="front__title">An<br>Integrated Path to<br>Operational Results<br>Growth</h1>
      <p class="front__subtitle">Shape a Steady Progress method<br>to match your workplace values</p>
      <div class="front__author-band">
        <span class="front__author">Martin Varrow B. Mech Eng., M. Sc (HTU)</span>
      </div>
    </div>
  </div>
</div>
</body>
</html>
```